Lorvika.no is a new website about pedagogical entrepreneurship. It's main target group is teachers. The Fjellmark Institute for Classroom Media and the Nordvik Agency for Schools and Study are leading the project.

The web page is meant to show examples of how different methods of entrepreneurship can be used pedagogical in a learning environment. The page will also support the user with examples of different teaching programs and other examples of best practice.

Pedagogical entrepreneurship is not about business and men in suits. It's a method for learning. The focus in the design should be on school, education and new ways of learning.

The final product should be motivating and engaging, but at the same time governmental and serious. We are not looking for something "flashy" and corporate-looking, but a moderate, task-focused and clean design that state quality.

We need designs for three pages:
1 - frontpage
2 - subpage ("Metoder og undervisningsopplegg")
3 - subpage ("Smått-VERK i Brekkelia")

The interaction design for these three pages will be uploaded as an attachment.

We would like you to find inspiration in the following websites:
- www.gryvekst.no
- www.lavrek.no
- www.tovandstudio.com
- www.kvp.no
(more will be added)

Please use the attached logo, and feel free to use this as an inspiration for the rest of the design.

Target Market(s)

Teachers

Industry/Entity Type

Education

Requirements
Must have
• * Header with: Logo. Main navigation. Utility navigation. Search box.
* Footer
Should not have
• Images of men in suits.
Very strong graphical elements that stands out too much (we want it clean).

```html
<!DOCTYPE html>
<html lang="en">
<head>
<meta charset="utf-8">
<title>Lorvika.no – Pedagogical entrepreneurship</title>
<link rel="stylesheet" href="https://fonts.googleapis.com/css2?family=Arimo:ital,wght@0,400;0,700;1,400&display=swap">
<style>
:root{
  --navy:#0b4677;
  --navy-deep:#093a66;
  --sky:#bfe3f3;
  --sky-pale:#eef8fd;
  --accent:#3a9ad4;
  --accent-light:#45b8e8;
  --link-dark:#1b5a93;
  --text-grey:#555;
  --footer-top:#1f4d7c;
  --footer-bottom:#1c3b66;
  --footer-link:#bfe2fb;
  --white:#fff;
}
*{box-sizing:border-box;margin:0;padding:0}
html,body{width:1115px;height:1200px;overflow:hidden}
body{font-family:"Arimo",Arial,sans-serif;position:relative;background:var(--sky)}
.abs{position:absolute}
a{color:inherit;text-decoration:none}

/* header */
.site-header{left:0;top:0;width:1115px;height:318px;
  background:radial-gradient(ellipse 600px 300px at 560px 140px,#1e5f95 0%,var(--navy) 60%,var(--navy-deep) 100%)}
.utility-nav{top:9px;left:485px;font-size:13px;color:var(--white)}
.utility-nav a{position:absolute;white-space:nowrap}
.search-box{left:847px;top:7px;width:126px;height:20px;background:var(--white);border-radius:3px}
.search-btn{left:973px;top:7px;width:20px;height:20px}
.brand-mark{left:30px;top:50px;width:70px;height:70px;border-radius:50%;background:var(--accent-light)}
.brand-name{left:133px;top:42px;font-size:52px;font-weight:700;color:var(--accent-light);letter-spacing:-1px}
.intro{left:421px;top:78px;width:600px;font-size:14px;font-style:italic;color:var(--white);line-height:16px}
.intro a{font-style:normal;font-weight:700;font-size:12px;color:var(--accent-light)}
.intro-rule{left:421px;top:112px;width:694px;height:1px;background:var(--accent-light)}
.main-nav .icon{width:80px;height:76px;border-radius:6px;background:linear-gradient(180deg,#8ea3b5,#d8dfe6)}
.main-nav .kicker{font-size:12px;font-style:italic;color:var(--accent-light)}
.main-nav .title{font-size:18px;font-weight:700;color:var(--white);line-height:18px;margin-top:5px}

/* content */
.content-bg{left:0;top:318px;width:1115px;height:604px;
  background:radial-gradient(ellipse 520px 300px at 560px 760px,var(--white) 0%,var(--sky-pale) 35%,var(--sky) 100%)}
.meter-card{left:66px;top:336px;width:270px;height:315px;border:1px solid var(--accent);border-radius:5px;
  background:radial-gradient(circle at 150px 160px,var(--white) 40%,#dde3e8 100%)}
.tag{background:var(--accent);color:var(--white);box-shadow:2px 2px 3px rgba(0,0,0,.25)}
.meter-tag{left:54px;top:352px;width:256px;height:48px;padding:5px 6px 4px 30px;font-size:19px;font-style:italic;line-height:18px;white-space:nowrap}
.meter-art{left:116px;top:414px;width:160px;height:166px;border-radius:50%;
  background:radial-gradient(circle,#f3efe7 30%,#2e6fb3 62%,#1b3f73 100%)}
.meter-link{left:139px;top:618px;font-size:18px;color:#2a7fc0}

.start-card{left:347px;top:336px;width:681px;height:318px;background:var(--white);border:1px solid var(--accent);border-radius:5px}
.start-title{left:387px;top:364px;font-size:28px;color:var(--accent-light);font-weight:400}
.col-head{font-size:22px;font-weight:700;color:var(--text-grey);top:401px}
.link-list{top:427px;width:190px}
.link-list .rail{position:absolute;left:6px;top:0;width:1px;height:148px;background:var(--accent)}
.link-list li{list-style:none;position:absolute;left:6px;font-size:15px;color:var(--text-grey);padding-left:39px;white-space:nowrap}
.link-list li::before{content:"";position:absolute;left:0;top:9px;width:36px;height:1px;background:var(--accent)}
.see-more{font-size:15px;font-weight:700;color:var(--text-grey);top:598px}

.inspiration{left:119px;top:680px;width:865px;height:188px;background:var(--white);border:1px solid #c9d6df;border-radius:5px}
.insp-tag{left:99px;top:699px;width:195px;height:44px;padding:8px 35px;font-size:22px;font-weight:700}
.insp-caption{left:130px;top:815px;width:181px;text-align:right;font-size:20px;color:var(--link-dark);line-height:22px}
.insp-photo{left:336px;top:686px;width:599px;height:172px;
  background:linear-gradient(180deg,#7d9ec4 0%,#cdd8e2 22%,#52636a 42%,#3e5a2c 62%,#5d7a33 100%)}
.arrow{width:34px;height:34px}

/* footer */
.site-footer{left:0;top:922px;width:1115px;height:278px;background:linear-gradient(180deg,var(--footer-top),var(--footer-bottom))}
.footer-band{left:150px;top:922px;width:798px;height:278px;background:rgba(255,255,255,.06)}
.f-head{font-size:14px;font-weight:700;color:var(--white)}
.f-list{list-style:none;font-size:12px;color:var(--footer-link);line-height:22px}
.f-list .more{font-weight:700;color:var(--white)}
</style>
</head>
<body>

<header class="abs site-header"></header>
<nav class="abs utility-nav" aria-label="Utility">
  <a style="left:0">Best practice schools</a>
  <a style="left:144px">Lorvimeter</a>
  <a style="left:252px">About lorvika.no</a>
</nav>
<div class="abs search-box" role="search"></div>
<svg class="abs search-btn" viewBox="0 0 20 20" aria-label="Search">
  <circle cx="10" cy="10" r="10" fill="#123a60"/>
  <circle cx="11" cy="8" r="3.5" fill="none" stroke="#fff" stroke-width="1.6"/>
  <line x1="8.5" y1="10.5" x2="5" y2="14" stroke="#fff" stroke-width="2"/>
</svg>

<div class="abs brand-mark"></div>
<div class="abs brand-name">Lorvika</div>

<p class="abs intro">Pedagogical entrepreneurship works. Lorem ipsum dolor sit amet, consectetur adipisicing elit, sed do eusmod tempor incididunt ut labore ed dolore magna aliqua. <a>Learn more&gt;</a></p>
<div class="abs intro-rule"></div>

<nav class="main-nav" aria-label="Main">
  <div class="abs icon" style="left:162px;top:180px" role="img" aria-label="Illustration of a stack of books"></div>
  <div class="abs" style="left:255px;top:184px"><div class="kicker">Learn about waht, why and how!</div><div class="title">What is pedagogical<br>enterpreneurship?</div></div>
  <div class="abs icon" style="left:462px;top:180px" role="img" aria-label="Illustration of an open planner with a pen"></div>
  <div class="abs" style="left:563px;top:184px"><div class="kicker">Plan your lessons!</div><div class="title">Methods and<br>teaching plans</div></div>
  <div class="abs icon" style="left:716px;top:172px" role="img" aria-label="Illustration of an inkwell with a quill"></div>
  <div class="abs" style="left:802px;top:182px"><div class="kicker">Be inspired</div><div class="title">Good examples<br>Best practice</div></div>
</nav>

<main>
  <div class="abs content-bg"></div>

  <section>
    <div class="abs meter-card"></div>
    <div class="abs tag meter-tag">Are you working<br>enterpreneurship-like?</div>
    <div class="abs meter-art" role="img" aria-label="Illustration of a compass-style meter"></div>
    <a class="abs meter-link">Try the lorvimeter!</a>
  </section>

  <section>
    <div class="abs start-card"></div>
    <h2 class="abs start-title">Get started!</h2>

    <h3 class="abs col-head" style="left:387px">Methods</h3>
    <ul class="abs link-list" style="left:387px"><span class="rail"></span>
      <li style="top:12px">Café-pedagogikk</li><li style="top:43px">Elevbedrift</li><li style="top:75px">Gründercamp</li><li style="top:107px">Story line</li><li style="top:138px">REAL</li>
    </ul>
    <a class="abs see-more" style="left:433px">See more...</a>

    <h3 class="abs col-head" style="left:593px">Teaching plans</h3>
    <ul class="abs link-list" style="left:592px"><span class="rail"></span>
      <li style="top:12px">Teaching plan title</li><li style="top:43px">Teaching plan title</li><li style="top:75px">Teaching plan title</li><li style="top:107px">Teaching plan title</li><li style="top:138px">Teaching plan title</li>
    </ul>
    <a class="abs see-more" style="left:639px">See more...</a>

    <h3 class="abs col-head" style="left:824px">Other section</h3>
    <ul class="abs link-list" style="left:823px"><span class="rail"></span>
      <li style="top:12px">Lorem ipsum dolor</li><li style="top:43px">Lorem ipsum dolor</li><li style="top:75px">Lorem ipsum dolor</li><li style="top:107px">Lorem ipsum dolor</li><li style="top:138px">Lorem ipsum dolor</li>
    </ul>
    <a class="abs see-more" style="left:870px">See more...</a>
  </section>

  <section>
    <div class="abs inspiration"></div>
    <div class="abs tag insp-tag">Inspiration</div>
    <p class="abs insp-caption">Smått-VERK at Brekkelia School</p>
    <div class="abs insp-photo" role="img" aria-label="Photo of a fjord landscape with mountains and a sculpture on a meadow"></div>
    <svg class="abs arrow" style="left:296px;top:754px" viewBox="0 0 34 34" aria-label="Previous">
      <circle cx="17" cy="17" r="16" fill="#fff" stroke="#9fc3df" stroke-width="1.5"/><circle cx="17" cy="17" r="13" fill="#1f64b0"/><path d="M11 17 L21 10 L21 24 Z" fill="#fff"/>
    </svg>
    <svg class="abs arrow" style="left:939px;top:754px" viewBox="0 0 34 34" aria-label="Next">
      <circle cx="17" cy="17" r="16" fill="#fff" stroke="#9fc3df" stroke-width="1.5"/><circle cx="17" cy="17" r="13" fill="#1f64b0"/><path d="M23 17 L13 10 L13 24 Z" fill="#fff"/>
    </svg>
  </section>
</main>

<footer class="abs site-footer"></footer>
<div class="abs footer-band"></div>
<div class="abs" style="left:206px;top:937px">
  <div class="f-head">Pedagogical entrepreneurship</div>
  <ul class="f-list" style="margin-top:2px">
    <li>What is pedagogical entrepreneurship?</li><li>Science</li><li>Best practice schols</li><li>Lorvimeter</li><li style="margin-top:16px">About lorvika.no</li>
  </ul>
</div>
<div class="abs" style="left:525px;top:934px">
  <div class="f-head">Methods</div>
  <ul class="f-list" style="margin-top:2px"><li>Story line</li><li>REAL</li><li>Café-pedagogikk</li><li class="more">See more...</li></ul>
  <div class="f-head" style="margin-top:22px">Teaching plans</div>
  <ul class="f-list" style="margin-top:2px"><li>Title</li><li>Title</li><li>Title</li><li class="more">See more...</li></ul>
</div>
<div class="abs" style="left:733px;top:934px">
  <div class="f-head">Gode eksempler</div>
  <ul class="f-list" style="margin-top:2px"><li>Smått-VERK i Brekkelia</li><li>Smått-VERK i Brekkelia</li><li>Smått-VERK i Brekkelia</li><li class="more">See more...</li></ul>
</div>

</body>
</html>
```